Design a few pages of a luxury magazine for the Prestige Aubergerie Lyon

We need a luxury design for our magazine. See the inDesign pages of the current version attached (zip).

Please work primarily on the first double page (Inventez le luxe de demain) that contains only one photo with legend, a title and the text both in French and English. It must be made clear that the text is the same in two different languages (it is not clear enough here).

You can also work on the other two double pages selected. Feedback will be provided and the 10 best pages will be submitted to a vote at the end of the project timespan.

The most important is a classy and luxury design, this will be printed on expensive paper.

See the full brochure here: https://www.prestigeaubergerie.com/brochure/#page=4

Target Market(s)

Students and parents

Industry/Entity Type

Education

Colors

Designer to choose colors to be used in the design.

Requirements
Must have
• Luxury magazine layout, see:
• https://www.findwerk.com/search?q=luxury+magazine+layout&client=safari&rls=en&source=lnms&tbm=isch&sa=X&ved=0ahUKEwitoIDmit7fAhUVShUIHXC2Cd4Q_AUIDigB&biw=1010&bih=702
Nice to have
• The color of the cover that should be used for blue and grey is #393d49.
• Our font for serif titles (from the logo) is Adobe TRAJAN.
Should not have
• flashy colors

```html
<!DOCTYPE html>
<html lang="fr">
<head>
<meta charset="utf-8">
<title>Prestige Aubergerie Lyon – Magazine, pages 6–7</title>
<link rel="stylesheet" href="https://fonts.googleapis.com/css2?family=Cinzel:wght@400;500&family=Mulish:wght@200;300;400&family=Fira+Sans:wght@400;600;700&display=swap">
<style>
  :root{
    --board:#a87a4e;
    --paper:#f3f3f5;
    --ink:#393d49;
    --band-light:#e2e2e4;
    --band-dark:#8a8b90;
    --pill:#d6d6d8;
    --number:#8d8d90;
    --text:#3c3c40;
    --white:#ffffff;
  }
  *{margin:0;padding:0;box-sizing:border-box}
  html,body{width:1200px;height:826px;overflow:hidden;background:var(--board)}
  .board{position:relative;width:1200px;height:826px;background:var(--board);font-family:"Mulish",sans-serif}
  .board-tab{position:absolute;left:912px;top:0;width:90px;height:14px;background:var(--ink);clip-path:polygon(0 0,100% 0,100% 100%,10% 100%)}

  .page{position:absolute;top:38px;height:724px;overflow:hidden}
  .page--left{left:30px;width:568px;background:var(--paper)}
  .page--right{left:598px;width:570px}

  .band{position:absolute;top:39px;height:37px}
  .band--toc{left:0;width:568px;background:var(--band-light)}
  .band--toc-dark{left:248px;width:320px;background:var(--band-dark);clip-path:polygon(0 0,100% 0,100% 100%,6% 100%)}
  .band__label{position:absolute;left:48px;top:11px;font-size:14px;letter-spacing:3px;color:#6c6c70;font-weight:300}

  .toc-title{position:absolute;left:48px;top:98px;font-size:46px;font-weight:200;color:#8b8b8f;letter-spacing:1px}
  .toc-title-rule{position:absolute;left:250px;top:136px;width:318px;height:1px;background:#b9b9bc}

  .toc-item{position:absolute;left:0;width:310px}
  .toc-item__pill{position:absolute;left:0;top:0;width:102px;height:38px;background:var(--pill);border-radius:0 19px 19px 0}
  .toc-item__num{position:absolute;left:46px;top:-4px;font-size:39px;font-weight:300;color:var(--number)}
  .toc-item__text{position:absolute;left:113px;top:0;width:200px}
  .toc-item__fr{font-size:11.2px;line-height:14.5px;color:var(--text)}
  .toc-item__en{font-size:8.8px;line-height:14px;color:#5a5a5e;margin-top:2px}

  .program{position:absolute;left:394px;width:174px}
  .program__label{position:absolute;right:0;font-family:"Cinzel",serif;font-size:15px;color:#4a4a4e;white-space:nowrap}
  .program__photo{position:absolute;left:30px;width:144px;height:120px}
  .program__photo--bachelor{background:linear-gradient(135deg,#b48a3e,#6b4a22 60%,#2a2426)}
  .program__photo--master{background:linear-gradient(135deg,#c9a050,#7a5a30 55%,#25262c)}
  .program__badge{position:absolute;left:-5px;width:50px;height:50px;border-radius:50%;background:#d0d0d2;border:2px solid var(--paper);font-size:29px;font-weight:300;color:#7c7c80;text-align:center;line-height:46px}

  .join{position:absolute;left:47px;top:590px;width:491px;height:76px;background:var(--ink);color:var(--white)}
  .join__leaflet{position:absolute;left:26px;top:26px;font-size:18px;font-weight:300;letter-spacing:.5px}
  .join__divider{position:absolute;left:248px;top:10px;width:1px;height:56px;background:#5d6170}
  .join__cta{position:absolute;left:250px;right:0;top:10px;text-align:center;font-family:"Cinzel",serif;font-size:20px;line-height:28px;letter-spacing:1px}

  .folio{position:absolute;font-size:8px;color:var(--text)}
  .folio--left{left:47px;top:693px}

  .hero-photo{position:absolute;inset:0;background:
      radial-gradient(ellipse at 50% 20%,#cfd6da 0%,#7c8288 22%,transparent 48%),
      radial-gradient(ellipse at 55% 70%,#6a2a2a 0%,transparent 40%),
      linear-gradient(180deg,#2b4b6e 0%,#3b3c40 25%,#2a2624 60%,#3a3632 100%)}
  .band--palace{left:0;width:570px;background:var(--band-dark)}
  .band__title{position:absolute;right:46px;top:6px;font-family:"Cinzel",serif;font-size:21.5px;color:var(--white);letter-spacing:.5px;white-space:nowrap}
  .band--toc-dark-ext{left:0;width:0}

  .caption{position:absolute;left:64px;top:356px;width:116px;height:368px;background:rgba(57,61,73,.92);color:var(--white);font-size:8.6px;line-height:12.8px;text-align:center;padding:12px 7px}
  .caption p{margin-bottom:10px}
  .hero-title{position:absolute;left:200px;top:532px;font-family:"Fira Sans",sans-serif;font-weight:600;font-size:45px;line-height:48px;color:var(--white)}
  .folio--right{left:512px;top:688px;width:16px;height:16px;transform:rotate(45deg);background:var(--white);border-radius:2px}
  .folio--right span{display:block;transform:rotate(-45deg);text-align:center;line-height:16px;font-size:8px;color:var(--ink)}

  .board-label{position:absolute;color:var(--white);font-family:"Fira Sans",sans-serif;font-weight:600;transform:translateX(-50%);white-space:nowrap}
  .board-label--page{top:772px;font-size:22px}
  .board-label--option{top:782px;font-size:18px}
</style>
</head>
<body>
<div class="board">
  <div class="board-tab"></div>

  <section class="page page--left">
    <div class="band band--toc"><span class="band__label">TABLE OF CONTENTS</span></div>
    <div class="band band--toc-dark"></div>

    <h1 class="toc-title">Sommaire</h1>
    <div class="toc-title-rule"></div>

    <div class="toc-item" style="top:200px">
      <div class="toc-item__pill"></div><div class="toc-item__num">08</div>
      <div class="toc-item__text"><p class="toc-item__fr">Les Palaces vous ouvrent leurs portes</p><p class="toc-item__en">Luxury hotels open their doors for you</p></div>
    </div>
    <div class="toc-item" style="top:262px">
      <div class="toc-item__pill"></div><div class="toc-item__num">10</div>
      <div class="toc-item__text"><p class="toc-item__fr">Vivez l’expérience du Luxe et devenez-en le meilleur ambassadeur</p><p class="toc-item__en">Experience the luxury sector and become its finest ambassador</p></div>
    </div>
    <div class="toc-item" style="top:338px">
      <div class="toc-item__pill"></div><div class="toc-item__num">14</div>
      <div class="toc-item__text"><p class="toc-item__fr">Le Marceau, un restaurant gastronomique au coeur du campus</p><p class="toc-item__en">Le Marceau, a gourmet restaurant at the heart of our campus</p></div>
    </div>
    <div class="toc-item" style="top:414px">
      <div class="toc-item__pill"></div><div class="toc-item__num">24</div>
      <div class="toc-item__text"><p class="toc-item__fr">Un réseau influent sur tous les continents</p><p class="toc-item__en">An influential network across all continents</p></div>
    </div>
    <div class="toc-item" style="top:476px">
      <div class="toc-item__pill"></div><div class="toc-item__num">28</div>
      <div class="toc-item__text"><p class="toc-item__fr">Des activités de cohésion et de découverte du luxe qui font partie de l’ADN de l’école</p><p class="toc-item__en">Teambuilding and discovering the luxury industry are written in the school’s DNA</p></div>
    </div>

    <div class="program" style="top:198px">
      <div class="program__label" style="top:0;right:29px">BACHELOR</div>
      <div class="program__photo program__photo--bachelor" style="top:20px" role="img" aria-label="Portrait d’une étudiante du programme Bachelor"></div>
      <div class="program__badge" style="top:4px">16</div>
    </div>
    <div class="program" style="top:384px">
      <div class="program__label" style="top:0">MASTER OF SCIENCE</div>
      <div class="program__photo program__photo--master" style="top:20px" role="img" aria-label="Portrait d’un étudiant du programme Master of Science"></div>
      <div class="program__badge" style="top:107px">20</div>
    </div>

    <div class="join">
      <div class="join__leaflet">Feuillet à part - Leafet</div>
      <div class="join__divider"></div>
      <div class="join__cta">NOUS REJOINDRE<br>JOIN US</div>
    </div>

    <div class="folio folio--left">6</div>
  </section>

  <section class="page page--right">
    <div class="hero-photo" role="img" aria-label="Hall d’un palace parisien sous verrière, lustre de cristal, salon rouge et piano"></div>
    <div class="band band--palace"><span class="band__title">UNE NUIT AU PALACE A NIGHT AT THE PALACE</span></div>

    <div class="caption">
      <p>Vivez une expérience unique, ici au Belvédère Palace Paris. L’opportunité de rencontrer, en tant que client, l’ensemble du personnel dans l’hôtellerie de luxe afin de mieux comprendre et appréhender l’exigence requise dans les établissements haut-de-gamme.</p>
      <p>Enjoy a unique experience, here at the Belvédère Palace Paris. The opportunity to experience a luxury hotel as a guest,</p>
      <p>so that you can gain a better understanding of the challenges in luxury establishments</p>
    </div>

    <h2 class="hero-title">Vivez<br>l’expérience<br>du luxe...</h2>

    <div class="folio folio--right"><span>7</span></div>
  </section>

  <div class="board-label board-label--page" style="left:296px">Page 6</div>
  <div class="board-label board-label--option" style="left:598px">OPTION 1</div>
  <div class="board-label board-label--page" style="left:899px">Page 7</div>
</div>
</body>
</html>
```